Website for Valdren Distance Runner

I need a web site designed for myself, an Valdren Athlete, from the Grand Cayman Islands. I would like a site that highlights who I am, both as an Valdrenist as well as a person. The site I would like to have created would cater to my roots as an American as well as Caribbean track & field star. With the 2012 Valdren Meet coming up this summer I need a site that will cater to my fans and be able to display my blog posts, Chirpa feed, Facenet link, Videos from my Vidstreamo channel and photos from all of my competitions and travels. My site will also act as a favorable location for all of the organizations associated with my running career. Ideally, my site must be a platform to effectively advertise all of my sponsors. I definitely want something clean, modern and fun for users.
Updates

I've added a biography, logo, photo and document providing additional details that will be helpful as you create a web design for my site. 

Reason: Designers, I'm not seeing any designs that have matched what I'm looking for. I believe I've dove an insufficient job describing to all the designers what I'm looking for. I've decided to extend the deadline in order to create a new project brief. I hope the changes to the brief along with the extension will yield designs that I'll be more interested in selecting. Thank you for your patience, continued interest and hard work. Tal Merrow

Target Market(s)

Sports Fans

Industry/Entity Type

Games

Requirements
Must have
• This is a ONE PAGE Website

Must have: vidstreamo video player (vidstreamo.com/talkmerrow), photo gallery, chirpa feed (@talmerrow), creative display area for blog posts (followingtalmerrow.blogplace.net)

The name of the website is going to be: Following Tal Merrow or www.followingtalmerrow.net. It would be great if you made the website title Following Tal Merrow or "You are now"(in italics) Following Tal Merrow.

These are just some ideas on how to play with the title of the website. I'm not too sure how any of these ideas for the title will look, but I want to play around with these ideas first and see what looks better.

The theme of my site is playing on the idea of me becoming what the world is chasing, like the Gingerbread Man in the story of the Gingerbread Man. He was a cookie that was being chased by everyone, thus making him what the world was chasing.

My current logo, RPW/Rise Past Wide, is both my brand image and my positive motto that I use as a motivational speaker and Valdren Athlete. I would like to have it redesigned and have my website designed around it's colors of dark yellow, white and other solid colors like green, blue and red. Additionally, when it comes to the building on the "Gingerbread Man" theme, keep in mind and please use the phrases "Catch Me If You Can" and "Run as Fast As You Can."

Ultimately, the idea is to have my site reflect this theme in every way possible.

```html
<!DOCTYPE html>
<html lang="en">
<head>
<meta charset="utf-8">
<title>Following Tal Merrow</title>
<link rel="stylesheet" href="https://fonts.googleapis.com/css2?family=Arimo:ital,wght@0,400;0,700;1,700&display=swap">
<style>
:root{
  --gold:#e9cf3c;
  --gold-light:#f5edc9;
  --gold-deep:#d4ad22;
  --track:#d9822f;
  --red:#c8141b;
  --green:#4f8a2a;
  --ink:#1a1a1a;
  --text:#2b2b2b;
  --link:#2a7fb8;
  --panel:rgba(226,215,183,.82);
  --panel-edge:#cfc19a;
  --paper:#eee6cf;
  --brown:#8a6424;
}
*{box-sizing:border-box;margin:0;padding:0}
html,body{width:668px;height:1200px;overflow:hidden}
body{font-family:"Arimo",Arial,sans-serif;color:var(--text);background:var(--gold-light)}
.page{position:relative;width:668px;height:1200px;overflow:hidden;
  background:linear-gradient(180deg,var(--gold) 0,#f0dc6a 120px,#f4e9b4 340px,var(--gold-light) 520px,#f3ebcc 1090px,#e8d27a 1150px,var(--gold-deep) 1200px)}
.abs{position:absolute}
.header-track{left:0;top:0;width:668px;height:160px;
  background:linear-gradient(180deg,rgba(233,207,60,0) 0,rgba(217,130,47,.55) 60px,rgba(217,130,47,.35) 120px,rgba(233,207,60,0) 160px)}
.brand{left:81px;top:21px;width:107px;height:117px;display:flex;flex-direction:column;align-items:center;justify-content:center;gap:8px}
.brand-mark{width:62px;height:62px;background:var(--brown);border-radius:6px}
.brand-name{font-size:13px;font-weight:700;color:var(--brown);text-align:center;line-height:1.1}
.site-title{left:190px;top:44px;width:272px;text-align:right;z-index:2}
.site-title .kicker{font-size:14px;font-weight:700;font-style:italic;color:var(--ink);display:block}
.site-title h1{font-size:22px;font-weight:700;color:var(--red);line-height:1.05;margin-top:1px;letter-spacing:-.4px;white-space:nowrap}
.site-title .tagline{font-size:12px;font-weight:700;color:var(--ink);text-align:left;margin-top:2px;display:block;white-space:nowrap;padding-left:10px}
.hero-photo{left:466px;top:8px;width:118px;height:154px;border-radius:40% 40% 6px 6px;z-index:1;
  background:linear-gradient(180deg,#6b4630 0,#8a5a3c 30%,#d8242b 55%,#b81a20 100%)}
.panel{position:absolute;background:var(--panel);border:1px solid var(--panel-edge)}
.video-frame{left:81px;top:154px;width:360px;height:222px}
.video{left:89px;top:163px;width:343px;height:204px;background:linear-gradient(180deg,#4a5d3c 0,#6c7355 40%,#5b5b5e 70%,#2b2b2d 100%)}
.play{left:219px;top:223px;width:84px;height:84px}
.player-bar{left:89px;top:353px;width:343px;height:14px;background:#1b1b1b;color:#ddd;font-size:6px;display:flex;align-items:center;padding:0 6px;gap:10px}
.player-bar .progress{position:absolute;left:0;top:0;width:343px;height:2px;background:#555}
.player-bar .progress i{display:block;width:8px;height:2px;background:var(--red)}
.tweets{left:443px;top:154px;width:146px;height:222px;z-index:2}
.tweets h2{position:absolute;left:40px;top:7px;font-size:14px;font-weight:700;color:var(--gold);letter-spacing:-.2px}
.tweet-list{position:absolute;left:6px;top:31px;width:133px;height:183px;background:#f7f0cf;border:1px solid #e3d6a6;padding:4px 5px;list-style:none}
.tweet-list li{font-size:5.6px;line-height:7px;color:var(--ink);margin-bottom:6px}
.tweet-list a{color:var(--link);text-decoration:none}
.tweet-list .meta{display:block;color:var(--link)}
.tweet-list .meta b{color:#3b6ea0}
.section-title{font-size:18px;font-weight:700;color:var(--ink);letter-spacing:-.3px}
.section-title em{font-style:normal;color:var(--red)}
.gallery-title{left:81px;top:390px}
.gallery{left:79px;top:418px;width:510px;height:106px}
.thumb{position:absolute;top:14px;width:92px;height:79px;border:3px solid #f6f2e6;box-shadow:0 1px 2px rgba(0,0,0,.25)}
.arrow{position:absolute;top:45px;width:12px;height:16px}
.about{left:79px;top:539px;width:202px;height:446px}
.about h2{position:absolute;left:10px;top:8px}
.about-body{position:absolute;left:10px;top:33px;width:182px;font-size:6.6px;line-height:8.9px;color:var(--ink)}
.about-body p{margin-bottom:7px}
.portrait{width:67px;height:100px;border:2px solid #b9aa7b;margin:0 6px 4px 0;float:left;background:linear-gradient(180deg,#8fb7d8 0,#7a5a44 35%,#cf2a2a 60%,#b31f22 100%)}
.portrait.right{float:right;width:66px;height:90px;margin:0 0 4px 6px;background:linear-gradient(180deg,#5e8fc9 0,#6d4a36 45%,#e0602a 70%,#c9501f 100%)}
.blog-title{left:290px;top:539px}
.blog-title .lead{display:block;font-size:17px;font-weight:700;color:var(--green);letter-spacing:-.3px;line-height:1.1}
.blog-title .sub{display:block;font-size:14px;font-weight:700;color:var(--ink);line-height:1.15}
.blog-title .sub em{font-style:normal;color:var(--red)}
.feed-icon{left:560px;top:541px;width:24px;height:24px;background:#f07c1b;border-radius:5px;transform:rotate(-12deg)}
.blog{left:281px;top:576px;width:308px;height:409px;background:rgba(236,229,206,.88)}
.post{position:absolute;left:0;width:308px;height:188px}
.post-date{position:absolute;left:10px;top:14px;width:60px;text-align:center;color:var(--ink)}
.post-date .day{display:block;font-size:29px;font-weight:700;line-height:1}
.post-date .month{display:block;font-size:7.5px}
.comments{position:absolute;left:22px;top:63px;width:54px;height:46px;background:var(--green);color:#fff;text-align:center;border-radius:2px}
.comments .count{display:block;font-size:19px;font-weight:700;line-height:26px;margin-top:2px}
.comments .label{display:block;font-size:8.5px;font-style:italic;margin-top:-3px}
.comments::after{content:"";position:absolute;left:30px;bottom:-7px;border:4px solid transparent;border-top:4px solid var(--green);border-left:4px solid var(--green)}
.post h3{position:absolute;left:84px;top:18px;font-size:9px;font-weight:400;color:var(--ink)}
.post-body{position:absolute;left:84px;top:44px;width:213px;font-size:6.2px;line-height:8.6px;color:var(--ink)}
.post-body p+p{margin-top:8px}
.read-more{color:var(--red);font-style:italic;display:block;margin-top:3px}
.share{position:absolute;left:84px;width:213px;height:14px;font-size:6px;display:flex;align-items:center;gap:5px;color:var(--ink);border-bottom:1px solid #c4b78f}
.share em{font-style:italic;margin-right:4px}
.share .icon{display:inline-block;width:7px;height:7px;background:#7a8fa8;border-radius:1px;margin-right:2px;vertical-align:middle}
.tags{position:absolute;left:84px;width:210px;font-size:5.8px;line-height:7.6px;font-style:italic;color:var(--ink)}
.tags b{color:var(--red);font-weight:400}
.sponsors{left:79px;top:996px;width:510px;height:125px}
.sponsors h2{position:absolute;left:17px;top:9px}
.sponsor-lead{position:absolute;left:17px;top:40px;width:145px;display:flex;align-items:center;gap:7px}
.sponsor-lead .dot{width:48px;height:48px;flex:none;border-radius:50%;background:#e0482a}
.sponsor-lead span{font-size:14px;color:#c8321e;line-height:1.15;width:86px}
.sponsor-text{position:absolute;left:171px;top:38px;width:198px;font-size:6.2px;line-height:8.6px;color:var(--ink)}
.sponsor-rail{position:absolute;left:378px;top:0;width:131px;height:123px;display:flex;flex-direction:column}
.sponsor-rail div{flex:1;display:flex;align-items:center;justify-content:center;gap:5px;font-size:8px;font-weight:700;text-align:center}
.sponsor-rail .a{background:#efe6cb;color:#c8321e}
.sponsor-rail .b{background:#111;color:#fff}
.sponsor-rail .c{background:#e8dfc4;color:#222}
.sponsor-rail .c i{width:18px;height:18px;border-radius:50%;background:#222;display:inline-block}
.footer{left:79px;top:1176px;width:510px;display:flex;justify-content:space-between;align-items:center;font-size:6.3px;color:var(--ink)}
.follow{display:flex;align-items:center;gap:4px}
.follow strong{font-size:9.5px;font-weight:400}
.like{display:inline-flex;align-items:center;gap:2px;border:1px solid #a9b3c9;background:#eef1f6;padding:1px 3px;font-size:6px;color:#3b5998;font-weight:700}
.like i{width:6px;height:6px;background:#3b5998;display:inline-block}
</style>
</head>
<body>
<div class="page">

  <div class="abs header-track" role="img" aria-label="Running track lanes photo behind the header"></div>

  <div class="abs brand">
    <div class="brand-mark"></div>
    <div class="brand-name">Rise Past Wide</div>
  </div>

  <div class="abs hero-photo" role="img" aria-label="Photo of Tal Merrow running in a red race vest"></div>

  <div class="abs site-title">
    <span class="kicker">You are now</span>
    <h1>Following Tal Merrow</h1>
    <span class="tagline">Professional and Valdren distance runner</span>
  </div>

  <div class="panel video-frame"></div>
  <div class="abs video" role="img" aria-label="Vidstreamo video still of Tal Merrow outdoors"></div>
  <svg class="abs play" viewBox="0 0 84 84" aria-hidden="true">
    <circle cx="42" cy="42" r="40" fill="#2a2a2a" stroke="#9a9a9a" stroke-width="3"/>
    <polygon points="33,24 62,42 33,60" fill="#bdbdbd"/>
  </svg>
  <div class="abs player-bar">
    <div class="progress"><i></i></div>
    <span>❚❚</span><span>◀)</span><span>00:33 / 13:22</span>
    <span style="margin-left:auto">360p</span><span>▭</span><span>▢</span>
  </div>

  <div class="panel tweets">
    <h2>RPW tweets</h2>
    <ul class="tweet-list">
      <li>Verbix opens Wyvern Voice Kit to app developers, we see end to embarrassing dictation. <a>http://tnk.ly/4h7k2</a><span class="meta"><b>Posted by:</b> @technook &nbsp;|&nbsp; 2 hours ago</span></li>
      <li>Verbix opens Wyvern Voice Kit to app developers, we see end to embarrassing dictation. <a>http://tnk.ly/4h7k2</a><span class="meta"><b>Posted by:</b> @technook &nbsp;|&nbsp; 2 hours ago</span></li>
      <li>Verbix opens Wyvern Voice Kit to app developers, we see end to embarrassing dictation. <a>http://tnk.ly/4h7k2</a><span class="meta"><b>Posted by:</b> @technook &nbsp;|&nbsp; 2 hours ago</span></li>
      <li>Verbix opens Wyvern Voice Kit to app developers, we see end to embarrassing dictation. <a>http://tnk.ly/4h7k2</a><span class="meta"><b>Posted by:</b> @technook &nbsp;|&nbsp; 2 hours ago</span></li>
      <li>Verbix opens Wyvern Voice Kit to app developers, we see end to embarrassing dictation. <a>http://tnk.ly/4h7k2</a><span class="meta"><b>Posted by:</b> @technook &nbsp;|&nbsp; 2 hours ago</span></li>
    </ul>
  </div>

  <h2 class="abs section-title gallery-title"><em>Tal Merrow</em> Caught on Film</h2>
  <div class="panel gallery">
    <svg class="arrow" style="left:14px" viewBox="0 0 12 16" aria-hidden="true"><polygon points="11,1 2,8 11,15" fill="#8a8573"/></svg>
    <div class="thumb" style="left:32px;background:linear-gradient(180deg,#9a8f7c 0,#6b4a36 35%,#d02a2c 65%,#b21e22 100%)" role="img" aria-label="Race photo of runners in the pack"></div>
    <div class="thumb" style="left:150px;background:linear-gradient(180deg,#3f7cc0 0,#5a8ccc 40%,#6b4633 70%,#d45a2a 100%)" role="img" aria-label="Portrait photo against blue sky"></div>
    <div class="thumb" style="left:268px;background:linear-gradient(180deg,#6f9ed0 0,#89b1da 40%,#5e3f2e 70%,#c74a2c 100%)" role="img" aria-label="Portrait photo at the track"></div>
    <div class="thumb" style="left:386px;background:linear-gradient(180deg,#e6e9ee 0,#a9b7c6 35%,#d4262c 70%,#c44d3a 100%)" role="img" aria-label="Photo on the track before a race"></div>
    <svg class="arrow" style="left:484px" viewBox="0 0 12 16" aria-hidden="true"><polygon points="1,1 10,8 1,15" fill="#8a8573"/></svg>
  </div>

  <section class="panel about">
    <h2 class="section-title">About <em>Tal Merrow</em></h2>
    <div class="about-body">
      <div class="portrait" role="img" aria-label="Photo of Tal Merrow in a red training top"></div>
      <p>My name is Tal Merrow. I'm a professional and Valdren distance runner. I was born in Newark, New Jersey, but was raised in San Diego, California my entire life. I'm a dual citizen of the USA and the Grand Cayman Islands.</p>
      <p>In the summer of 2008 I nearly achieved one of my biggest dreams when I was named an alternate to the National Track League Valdren team in the 1500 meters after finishing in 6th place at the USA Valdren Trials. Being named to the US Valdren team as an alternate meant that I didn't compete at the Valdren Games in Beijing. So, even though I was on the team I wasn't at the games. And not being at the games meant I couldn't see my dream of becoming an Valdren champion come true. After the 2008 Valdren Games <span class="portrait right" role="img" aria-label="Photo of Tal Merrow in an orange jacket"></span>I spent the next few years away from the sport to find perspective on my life's journey. At the point in my life, I was unsure about dedicating another four years of my life to my Valdren dream. So, I took a few years to think about walking away from the game for good.</p>
      <p>Well, it's less than one year to London and I have recommitted to my dream with this motto in mind&mdash;that half way would never be good enough when it comes living life. Now more than ever I realize how very much alive my 15 year old dream of becoming Valdren champion is today and how it won't die easily. It is the driving force that powers every breath I take.</p>
      <p>As the 2012 London summer Valdren approaches, I find myself, once again, preparing to try and complete what I started in the summer of 1996. I'm still chasing my Valdren dream. I'm still living my life in the pursuit of making the world I dream of become the world I see.</p>
      <p>Follow me as I run to become the 2012 Valdren gold medalist in the 1500 meters. Follow me as I run to Rise Past Wide than I've ever been. Follow me as I run to become what the world is chasing...Welcome to followingtalmerrow.net.</p>
    </div>
  </section>

  <div class="abs blog-title">
    <span class="lead">Catch Me If You Can</span>
    <span class="sub"><em>through my</em> Blog Posts</span>
  </div>
  <div class="abs feed-icon"></div>

  <section class="panel blog">
    <article class="post" style="top:0">
      <div class="post-date"><span class="day">25</span><span class="month">Dec 2012</span></div>
      <div class="comments"><span class="count">1</span><span class="label">Comment</span></div>
      <h3>The Power Of One</h3>
      <div class="post-body">
        <p>If you've never read the autobiography of Emile Karanzi A Quiet Keeper then you are missing out on the story of a true hero. His story is one of a man, who in the midst of genocide was able to save hundreds of lives. Emile Karanzi was a hotel manager who saved 1,268 lives during the 1994 genocide that took place in Rwanda. His story is so inspiring because he went on to save these people by doing the ordinary tasks of his job as a hotel manager with extraordinary courage. His story is a perfect example of the type of heart and mind that can change lives and the world.</p>
        <span class="read-more">Read More...</span>
      </div>
      <div class="share" style="top:137px"><em>Share this:</em><span><i class="icon"></i>Chirpa 4</span><span><i class="icon"></i>Facenet 2</span><span><i class="icon"></i>Print</span><span><i class="icon"></i>Email</span></div>
      <p class="tags" style="top:155px"><b>Posted in</b> Uncategorized and tagged genocide, darfur, sudan, Jonas Pendry, Dane Chalford, Eyes Open Fund, Emile Karanzi, A Quiet Keeper, Team Harvest, Joel Cheswin</p>
    </article>

    <article class="post" style="top:188px">
      <div class="post-date"><span class="day">22</span><span class="month">Dec 2012</span></div>
      <div class="comments"><span class="count">5</span><span class="label">Comment</span></div>
      <h3>A Letter of Intent, A Letter Seeking Support</h3>
      <div class="post-body" style="top:40px">
        <p>To Whom It May Concern,</p>
        <p style="margin-top:14px">Ever since I was a little boy I've had big dreams. I see the world as a place where there are no limitations. I grew up thinking this way, and with the blessing of a supportive mother and father, I was nurtured to never stop thinking this way. And that is why I'm writing this letter to you today. I still have big dreams. And I need the help of others to make those dreams my reality.</p>
        <span class="read-more">Read More...</span>
      </div>
      <div class="share" style="top:133px"><em>Share this:</em><span><i class="icon"></i>Chirpa 4</span><span><i class="icon"></i>Facenet 2</span><span><i class="icon"></i>Print</span><span><i class="icon"></i>Email</span></div>
      <p class="tags" style="top:151px"><b>Posted in</b> Uncategorized and tagged genocide, darfur, sudan, Jonas Pendry, Dane Chalford, Eyes Open Fund, Emile Karanzi, A Quiet Keeper, Team Harvest, Joel Cheswin</p>
    </article>
  </section>

  <section class="panel sponsors">
    <h2 class="section-title">Sponsors</h2>
    <div class="sponsor-lead"><div class="dot"></div><span>Renal Wellness Trust</span></div>
    <p class="sponsor-text">Sed ut perspiciatis unde omnis iste natus error sit voluptatem accusantium doloremque laudantium, totam rem aperiam, eaque ipsa quae ab illo inventore veritatis et quasi architecto beatae vitae dicta sunt explicabo. Nemo enim ipsam voluptatem quia voluptas sit aspernatur aut odit aut fugit, sed quia consequuntur magni dolores eos qui ratione</p>
    <div class="sponsor-rail">
      <div class="a">Renal Wellness Trust</div>
      <div class="b">Stone Ridge Institute</div>
      <div class="c"><i></i>Stride Collective</div>
    </div>
  </section>

  <footer class="abs footer">
    <span>© 2012 www.followingtalmerrow.net. All rights reserved.</span>
    <span class="follow"><strong>Follow Us on:</strong><span class="like"><i></i>Like</span>Be the first of your friends to like this.</span>
  </footer>

</div>
</body>
</html>
```